Online business manager needs a website

I need a website designed and then coded. I am an online business manager serving a number of different industries providing administrative support to existing small businesses and helping solo practitioners get their new business up and running.

I didn't have a logo formally designed but have been using the attached avatar and wouldn't mind something that incorporated that.

The business doesn't have an official name, so I've just been using my name Lia Morvath, Online Business Manager or Lia Morvath, OBM. I've attached two documents that I have made previously for an example of content.

I would prefer the final site be in Wordpress.

Requirements
Must have
• A way to contact me, testimonials, list of services

```html
<!DOCTYPE html>
<html lang="en">
<head>
<meta charset="utf-8">
<title>Lia Morvath – Online Business Manager</title>
<link href="https://fonts.googleapis.com/css2?family=Playfair+Display:ital,wght@1,700&family=Poppins:wght@400;500;600&display=swap" rel="stylesheet">
<style>
:root{
  --green:#1c7f5c;
  --green-dark:#16704f;
  --green-band:#2f8b6b;
  --ink:#222;
  --text:#555;
  --grey:#f3f3f3;
  --btn:#2a2a2a;
  --btn-grey:#8e8e8e;
  --star:#f5b400;
}
*{box-sizing:border-box;margin:0;padding:0}
html,body{width:1200px;height:4587px;overflow:hidden;background:#fff}
body{position:relative;font-family:"Poppins",sans-serif;color:var(--ink)}
.abs{position:absolute}
.script{font-family:"Playfair Display",serif;font-style:italic;font-weight:700;color:#2d2d2d}
.rule{position:absolute;height:2px;width:80px;background:var(--green)}

/* brand */
.brand{display:flex;align-items:center;gap:12px}
.brand-mark{width:62px;height:62px;border-radius:50%;background:var(--green)}
.brand-name{font-weight:600;font-size:38px;line-height:1;color:var(--green);letter-spacing:1px}
.brand-tag{font-weight:500;font-size:13px;letter-spacing:2px;color:var(--green);margin-top:4px}

/* nav */
.nav{top:86px;left:512px;display:flex;gap:30px;font-size:14px;color:#333}

/* hero */
.hero-title{left:89px;top:298px;font-size:50px;line-height:72px}
.hero-text{left:89px;top:450px;width:360px;font-size:14px;line-height:26px;color:var(--text)}
.btn{position:absolute;display:flex;align-items:center;justify-content:center;color:#fff;font-size:14px;font-weight:500;background:var(--btn)}
.dots{left:89px;top:713px;display:flex;gap:10px}
.dots span{width:12px;height:12px;border-radius:50%;background:#c8c8c8}
.dots span:first-child{background:#222}
.hero-photo{left:507px;top:150px;width:660px;height:660px;border-radius:50%;background:radial-gradient(circle at 40% 45%,#555 0 22%,#d9d6d3 23% 60%,#ece9e6 61%)}

/* about */
.about-band{left:0;top:1057px;width:1200px;height:363px;background:var(--grey)}
.about-frame{left:89px;top:899px;width:303px;height:383px;background:#fff;border-radius:28px;box-shadow:0 4px 18px rgba(0,0,0,.15);padding:14px}
.about-photo{width:100%;height:100%;border-radius:22px;background:linear-gradient(160deg,#7a4a6a,#4a6a3a 50%,#2a2a2a)}
.about-title{left:454px;top:930px;font-size:48px}
.about-text{left:436px;top:1100px;width:646px;font-size:14.5px;line-height:26px;color:var(--text);text-align:justify}

/* services */
.services{left:0;top:1420px;width:1200px;height:736px;background:linear-gradient(135deg,#2b8767,#3a9373 50%,#2a8464)}
.services-title{left:0;width:1200px;top:1490px;text-align:center;font-size:48px;color:#fff}
.card{position:absolute;width:210px;height:186px;background:#fff;display:flex;flex-direction:column;align-items:center;justify-content:flex-end;padding-bottom:26px;text-align:center;font-size:17px;font-weight:500;line-height:22px;color:#333}
.card svg{margin-bottom:14px}

/* contact */
.contact-title{left:142px;top:2290px;font-size:48px}
.contact-item{position:absolute;left:160px;width:320px;text-align:center}
.contact-item .line{position:absolute;top:17px;width:270px;left:25px;height:1px;background:#bbb}
.contact-item .ico{position:relative;width:32px;height:32px;margin:0 auto;border-radius:50%;background:var(--green);display:flex;align-items:center;justify-content:center}
.contact-item p{font-size:22px;margin-top:8px;color:#222}
.contact-photo{left:637px;top:2295px;width:448px;height:448px;border-radius:50%;background:radial-gradient(circle,#c89a7a 0 35%,#3a3a7a 60%,#1b1b4a)}

/* testimonials */
.testi-title{left:0;width:1200px;top:2922px;text-align:center;font-size:48px}
.quote{position:absolute;width:317px;background:#fff;border-radius:18px;box-shadow:0 3px 14px rgba(0,0,0,.09);padding:34px 40px 30px}
.quote .mark{font-family:"Playfair Display",serif;font-size:34px;line-height:20px;font-weight:700;color:#333}
.quote p{font-size:14px;line-height:19px;color:#555;text-align:justify;margin-top:6px}
.person{position:absolute;display:flex;align-items:center;gap:14px}
.avatar{width:76px;height:76px;border-radius:50%;background:linear-gradient(160deg,#d9b08c,#8a5a3a)}
.person b{display:block;font-size:12px;font-weight:600}
.person small{display:block;font-size:9px;color:#666}
.stars{color:var(--star);font-size:11px;letter-spacing:1px}

/* portfolio */
.port-title{left:89px;top:3725px;font-size:48px}
.port-label{left:91px;top:3846px;font-size:14px;font-weight:500;letter-spacing:.5px}
.port-text{left:91px;top:3882px;width:360px;font-size:14.5px;line-height:26px;color:#444}
.tile{position:absolute;border:2px solid #ddd}

/* footer */
.footer{left:0;top:4238px;width:1200px;height:271px;background:var(--green)}
.footer-bar{left:0;top:4509px;width:1200px;height:78px;background:var(--green-dark)}
.footer-brand{left:420px;top:4300px}
.footer-brand .brand-mark{background:#fff}
.footer-brand .brand-name,.footer-brand .brand-tag{color:#fff}
.fcontacts{left:190px;top:4414px;display:flex;gap:46px;color:#fff;font-size:13px;align-items:center}
.fcontacts div{display:flex;align-items:center;gap:12px}
.fcontacts i{width:34px;height:34px;border-radius:50%;background:#fff;display:flex;align-items:center;justify-content:center}
.copy{left:89px;top:4536px;color:#fff;font-size:14px}
.fnav{right:89px;top:4536px;color:#fff;font-size:14px;display:flex;gap:14px}
</style>
</head>
<body>

<!-- header -->
<header class="abs brand" style="left:86px;top:58px">
  <div class="brand-mark"></div>
  <div><div class="brand-name">LIA MORVATH</div><div class="brand-tag">ONLINE BUSINESS MANAGER</div></div>
</header>
<nav class="abs nav"><span>HOME</span><span>ABOUT ME</span><span>SERVICES</span><span>TESTIMONIALS</span><span>CONTACT ME</span><span>PRICING</span></nav>

<!-- hero -->
<h1 class="abs script hero-title">Digital Business<br>Management</h1>
<p class="abs hero-text">Lorem ipsum dolor sit amet, con sectetur adipiscing elit. Quisque consectetur non</p>
<a class="btn" style="left:87px;top:532px;width:175px;height:68px">CONTACT ME</a>
<div class="abs dots"><span></span><span></span><span></span><span></span><span></span></div>
<div class="abs hero-photo" role="img" aria-label="Photo of hands typing on a laptop on a marble desk"></div>

<!-- about -->
<div class="abs about-band"></div>
<div class="abs about-frame"><div class="about-photo" role="img" aria-label="Portrait photo of Lia Morvath"></div></div>
<h2 class="abs script about-title">About Me</h2>
<div class="rule" style="left:452px;top:1011px"></div>
<p class="abs about-text">Hi! I'm so excited that you have chosen to explore my portfolio. Helping businesses achieve their goals is my passion, and I'm thrilled that with my assistance you will have more time for your own passion project. I thrive while working independently, which means you can be confident when eaving tasks for me. The type of work that lights me up is anything involving organization and/or spreadsheets. You need data analyzed that includes multiple nested if formulas? You have an overwhelming amountof email to sort through and appointments to book? I'm your gal!</p>

<!-- services -->
<section class="abs services" role="img" aria-label="Green tinted photo of people working at a desk with laptops and phones"></section>
<h2 class="abs script services-title">Services</h2>
<div class="rule" style="left:560px;top:1568px;background:#fff"></div>

<div class="card" style="left:87px;top:1639px"><svg width="56" height="70" viewBox="0 0 56 70" fill="none" stroke="var(--green)" stroke-width="2.5"><path d="M10 64l6-20 22-38 8 5-22 38z"/><path d="M24 66l4-18 18-34 7 4-18 34z"/></svg>Content<br>Repurposing</div>
<div class="card" style="left:365px;top:1639px"><svg width="56" height="44" viewBox="0 0 56 44" fill="none" stroke="var(--green)" stroke-width="3"><rect x="3" y="3" width="50" height="38"/><path d="M3 3l25 22 25-22"/></svg>Email<br>Management</div>
<div class="card" style="left:632px;top:1639px"><svg width="56" height="62" viewBox="0 0 56 62" fill="none" stroke="var(--green)" stroke-width="3"><circle cx="24" cy="24" r="20"/><path d="M38 38l14 18"/><text x="24" y="33" text-anchor="middle" font-family="Poppins" font-size="26" font-weight="600" fill="var(--green)" stroke="none">$</text></svg>Financial<br>Analytics</div>
<div class="card" style="left:901px;top:1639px"><svg width="60" height="50" viewBox="0 0 60 50" fill="none" stroke="var(--green)" stroke-width="2.5"><rect x="18" y="6" width="38" height="40"/><path d="M26 16h22M26 24h22M26 32h22"/><circle cx="12" cy="16" r="8"/><path d="M2 44c0-10 4-16 10-16s10 6 10 16"/></svg>Project<br>Management</div>

<div class="card" style="left:87px;top:1885px"><svg width="30" height="56" viewBox="0 0 30 56" fill="none" stroke="var(--green)" stroke-width="3"><rect x="8" y="3" width="14" height="28" rx="7" fill="var(--green)"/><path d="M3 24c0 10 5 16 12 16s12-6 12-16M15 40v12M8 52h14"/></svg>Graphic<br>Creations</div>
<div class="card" style="left:365px;top:1885px"><svg width="70" height="56" viewBox="0 0 70 56" fill="var(--green)"><rect x="22" y="2" width="46" height="28" rx="6"/><rect x="2" y="20" width="46" height="28" rx="6" stroke="#fff" stroke-width="3"/><path d="M10 46l-4 10 14-8z"/></svg>Book<br>keeping</div>
<div class="card" style="left:632px;top:1885px"><svg width="44" height="44" viewBox="0 0 44 44"><rect x="4" y="4" width="36" height="36" rx="6" fill="var(--green)"/></svg>Data Entry</div>
<div class="card" style="left:901px;top:1885px"><svg width="56" height="56" viewBox="0 0 56 56"><circle cx="28" cy="28" r="24" fill="none" stroke="var(--green)" stroke-width="4"/></svg>More<br>Awesomeness</div>

<!-- contact -->
<h2 class="abs script contact-title">Lets's Get In &nbsp;Touch</h2>
<div class="contact-item" style="top:2439px"><div class="line"></div><div class="ico"><svg width="16" height="16" viewBox="0 0 24 24" fill="#fff"><path d="M6.6 10.8a15 15 0 006.6 6.6l2.2-2.2c.3-.3.7-.4 1-.2 1.1.4 2.3.6 3.6.6.6 0 1 .4 1 1V20c0 .6-.4 1-1 1A17 17 0 013 4c0-.6.4-1 1-1h3.5c.6 0 1 .4 1 1 0 1.3.2 2.5.6 3.6.1.3 0 .7-.2 1z"/></svg></div><p>555.014.2286</p></div>
<div class="contact-item" style="top:2524px"><div class="line"></div><div class="ico"><svg width="16" height="12" viewBox="0 0 16 12" fill="none" stroke="#fff" stroke-width="1.6"><rect x="1" y="1" width="14" height="10"/><path d="M1 1l7 6 7-6"/></svg></div><p>lialynn7@example.com</p></div>
<div class="contact-item" style="top:2608px"><div class="line"></div><div class="ico"><svg width="12" height="12"><rect width="12" height="12" fill="#fff"/></svg></div><p>Lia Lynn Morvath</p></div>
<div class="abs contact-photo" role="img" aria-label="Portrait photo of Lia Morvath against a starry background"></div>

<!-- testimonials -->
<h2 class="abs script testi-title">Testimonials</h2>
<div class="rule" style="left:560px;top:3003px"></div>

<div class="quote" style="left:80px;top:3092px;height:254px"><div class="mark">“</div><p>When it became apparent that a project would take more time than I had, Lia stepped up to take othe required research. She was though and timely; able to meet a 12-hour deadline. I would highly recommend Lia to assist with your next project.</p></div>
<div class="person" style="left:86px;top:3365px"><div class="avatar" role="img" aria-label="Client photo"></div><div><b>Tessa R</b><small>Owner, Northgate Exteriors</small><span class="stars">★★★★★</span></div></div>

<div class="person" style="left:441px;top:3143px"><div class="avatar" role="img" aria-label="Client photo" style="background:linear-gradient(160deg,#e0d0c0,#3a3a4a)"></div><div><b>Dana Whitfield</b><small>COO, Worldwide</small><span class="stars">★★★★★</span></div></div>
<div class="quote" style="left:440px;top:3242px;height:197px"><div class="mark">“</div><p>Lorem ipsum dolor sit amet, conse ctetur adipiscing elit, sed do eiusmod tempor incididunt ut labore et dolore magna ut labore et dolore magna tempor incidi-</p></div>

<div class="quote" style="left:799px;top:3092px;height:254px"><div class="mark">“</div><p>When it became apparent that a project would take more time than I had, Lia stepped up to take othe required research. She was though and timely; able to meet a 12-hour deadline. I would highly recommend Lia to assist with your next project.</p></div>
<div class="person" style="left:805px;top:3365px"><div class="avatar" role="img" aria-label="Client photo"></div><div><b>Tessa R</b><small>Owner, Northgate Exteriors</small><span class="stars">★★★★★</span></div></div>

<!-- portfolio -->
<h2 class="abs script port-title">Portfolio</h2>
<div class="rule" style="left:89px;top:3806px"></div>
<div class="abs port-label">DIGITAL BUSINESS MANAGER</div>
<p class="abs port-text">focused on the live event and entertainment industry. Helping artists and owners to better manage their career and business by strategically reviewing systems, recommending operational efficiencies, and managing inboxes</p>
<a class="btn" style="left:89px;top:4051px;width:174px;height:70px">CONTACT ME</a>
<a class="btn" style="left:288px;top:4051px;width:175px;height:70px;background:var(--btn-grey)">PRICING</a>

<div class="tile" role="img" aria-label="Podcast promotion graphic" style="left:602px;top:3708px;width:240px;height:219px;background:linear-gradient(135deg,#f6ece6,#ffffff 60%,#e9e2dc)"></div>
<div class="tile" role="img" aria-label="Webinar promotion graphic" style="left:602px;top:3941px;width:240px;height:222px;background:linear-gradient(135deg,#fbe9e2,#f7d9cc)"></div>
<div class="tile" role="img" aria-label="Video call tips graphic on orange background" style="left:858px;top:3710px;width:256px;height:453px;background:linear-gradient(180deg,#f88a44 0 58%,#9a8a80 58%)"></div>

<!-- footer -->
<footer>
  <div class="abs footer"></div>
  <div class="abs brand footer-brand"><div class="brand-mark"></div><div><div class="brand-name">LIA MORVATH</div><div class="brand-tag">ONLINE BUSINESS MANAGER</div></div></div>
  <div class="abs fcontacts">
    <div><i><svg width="16" height="16" viewBox="0 0 24 24" fill="var(--green)"><path d="M6.6 10.8a15 15 0 006.6 6.6l2.2-2.2c.3-.3.7-.4 1-.2 1.1.4 2.3.6 3.6.6.6 0 1 .4 1 1V20c0 .6-.4 1-1 1A17 17 0 013 4c0-.6.4-1 1-1h3.5c.6 0 1 .4 1 1 0 1.3.2 2.5.6 3.6.1.3 0 .7-.2 1z"/></svg></i>555.014.2286</div>
    <div><i><svg width="16" height="12" viewBox="0 0 16 12" fill="none" stroke="var(--green)" stroke-width="1.6"><rect x="1" y="1" width="14" height="10"/><path d="M1 1l7 6 7-6"/></svg></i>lialynn7@example.com</div>
    <div><i><svg width="12" height="12"><rect width="12" height="12" fill="var(--green)"/></svg></i>Lia Lynn Morvath</div>
    <div><i><svg width="12" height="12"><circle cx="6" cy="6" r="6" fill="var(--green)"/></svg></i>/LiaLynn07</div>
  </div>
  <div class="abs footer-bar"></div>
  <div class="abs copy">Copyright @ 2023 All rights reserved</div>
  <div class="abs fnav"><span>ABOUT ME</span><span>|</span><span>SERVICES</span><span>|</span><span>TESTIMONIALS</span><span>|</span><span>CONTACT ME</span><span>|</span><span>PRICING</span></div>
</footer>

</body>
</html>
```